Business Card for: Northbrook Financial Advisory Services Inc.

provide strategic financial advisory services to companies in the areas of corporate finance, mergers and acquisitions, executive coaching and strategic planning

Target Market(s)

Companies, banks, accountants, lawyers

Industry/Entity Type

High end business consulting in corporate finance, mergers and acquisitions, consulting

Contact Information for Business Card

Name of company, Name: xxxxxx xxxxxx , CEO, - phone number: 1-xxx-xxx-xxxx, - email address,

Requirements
Must have
• Must be professional and simple.
Nice to have
• simple, straight graphics, must give the impression that we are trustworthy, professional, competent
Should not have
• loud colors, loud design features

```html
<!DOCTYPE html>
<html lang="en">
<head>
<meta charset="utf-8">
<title>Northbrook Financial Advisory Inc – Business Card</title>
<link rel="stylesheet" href="https://fonts.googleapis.com/css2?family=Poppins:wght@400;500;600&display=swap">
<style>
  :root {
    --stage: #3a3a3a;
    --card-black: #0b0b0b;
    --card-white: #ffffff;
    --ink: #1a1a1a;
    --ink-soft: #4a4a4a;
    --emboss: #222222;
    --band-text: #ffffff;
  }
  * { box-sizing: border-box; margin: 0; padding: 0; }
  html, body { width: 1200px; height: 689px; overflow: hidden; }
  body {
    background: var(--stage);
    font-family: "Poppins", sans-serif;
    display: flex;
    align-items: center;
    justify-content: center;
    gap: 60px;
  }
  .card {
    width: 525px;
    height: 300px;
    border-radius: 18px;
    overflow: hidden;
    position: relative;
    box-shadow: 0 12px 30px rgba(0,0,0,0.45);
  }
  /* Front */
  .card--front {
    background: var(--card-black);
    display: flex;
    align-items: center;
    justify-content: center;
  }
  .brand {
    display: flex;
    align-items: center;
    gap: 14px;
  }
  .brand__dot {
    width: 38px;
    height: 38px;
    border-radius: 50%;
    background: currentColor;
    flex: none;
  }
  .brand__name {
    font-weight: 500;
    line-height: 1.1;
  }
  .brand__name span { display: block; }
  .card--front .brand { color: var(--emboss); }
  .card--front .brand__name span:first-child { font-size: 46px; }
  .card--front .brand__name span:last-child { font-size: 21px; letter-spacing: 0.5px; }

  /* Back */
  .card--back {
    background: var(--card-white);
    display: flex;
    flex-direction: column;
  }
  .card__body {
    flex: 1;
    display: flex;
    flex-direction: column;
    align-items: center;
    justify-content: center;
    gap: 22px;
    padding-top: 8px;
  }
  .card--back .brand { color: var(--ink); }
  .card--back .brand__dot { width: 28px; height: 28px; }
  .card--back .brand__name span:first-child { font-size: 32px; }
  .card--back .brand__name span:last-child { font-size: 15px; letter-spacing: 0.4px; }
  .person { text-align: center; }
  .person__name { font-size: 22px; font-weight: 600; color: var(--ink); }
  .person__role { font-size: 15px; font-weight: 400; color: var(--ink-soft); }
  .contact-band {
    height: 62px;
    background: var(--card-black);
    color: var(--band-text);
    display: flex;
    align-items: center;
    justify-content: center;
    gap: 12px;
    font-size: 13.5px;
    font-weight: 400;
  }
  .contact-band__sep { opacity: 0.8; }
</style>
</head>
<body>
  <section class="card card--front" aria-label="Card front">
    <div class="brand">
      <span class="brand__dot"></span>
      <p class="brand__name"><span>Northbrook</span><span>Financial Advisory Inc</span></p>
    </div>
  </section>

  <section class="card card--back" aria-label="Card back">
    <div class="card__body">
      <div class="brand">
        <span class="brand__dot"></span>
        <p class="brand__name"><span>Northbrook</span><span>Financial Advisory Inc</span></p>
      </div>
      <div class="person">
        <p class="person__name">Daniel Hartley</p>
        <p class="person__role">Managing Director</p>
      </div>
    </div>
    <div class="contact-band">
      <span>044-555 017 342</span>
      <span class="contact-band__sep">|</span>
      <span>info@northbrookfa.com</span>
      <span class="contact-band__sep">|</span>
      <span>www.northbrookfa.com</span>
    </div>
  </section>
</body>
</html>
```